ORVET - Helping People with Disabilities

ORVET is a nonprofit that strives to enable people with physical disabilities to live meaningful, quality lives. ORVET needs a professional attractive website that:
• establishes a strong brand image
• presents Orvet's services to those who need it
• raises funds from potential donors
Please see WORD DOC attached for more information about design vision.

Target Market(s)

people with disabilities

Industry/Entity Type

charity website

Number of Pages Required

2 page

Font styles to use
Sans Serif

Requirements
Must have
• 1. 2 pages means 1 design for homepage and 1 design for top of inner pages (banner ideas)
Nice to have
• please see attached design brief (WORD DOC)

```html
<!DOCTYPE html>
<html lang="en">
<head>
<meta charset="utf-8">
<title>ORVET – A Good Life For Everyone</title>
<link rel="stylesheet" href="https://fonts.googleapis.com/css2?family=Josefin+Sans:wght@300;400;600;700&family=Nunito+Sans:wght@400;600;700;800&display=swap">
<style>
:root{
  --teal:#137a74;
  --teal-light:#1c8f87;
  --teal-dark:#0c3330;
  --orange:#f7941d;
  --ink:#2b2f33;
  --muted:#6b7378;
  --mist:#eef3f4;
  --line:#d7dfe1;
  --white:#ffffff;
  --map-top:#cfe6f4;
  --map-bottom:#a9cbe6;
}
*{box-sizing:border-box;margin:0;padding:0}
html,body{width:1200px;height:3720px;overflow:hidden}
body{position:relative;font-family:"Nunito Sans",sans-serif;color:var(--ink);background:var(--white)}
.abs{position:absolute}
h1,h2{font-weight:400}
.heading{font-family:"Josefin Sans",sans-serif;font-weight:300;letter-spacing:5px;color:var(--teal);text-transform:uppercase}
.btn{position:absolute;display:flex;align-items:center;justify-content:center;gap:8px;font-weight:700;font-size:12px;color:var(--white);background:var(--orange)}
.btn svg{width:14px;height:14px}
/* top bar */
.topbar{left:0;top:0;width:1200px;height:32px;background:var(--teal-dark)}
.topbar .social{top:8px;width:16px;height:16px;border:2px solid #cfd8d7;border-radius:3px}
.join{left:696px;top:9px;font-size:12px;font-weight:800;color:var(--white);letter-spacing:.5px}
.topbar .donate{left:813px;top:0;width:155px;height:32px;letter-spacing:1px;font-size:12px}
/* header */
.header{left:0;top:32px;width:1200px;height:79px;background:var(--white)}
.brand{left:235px;top:26px;display:flex;align-items:center;gap:8px;font-weight:800;font-size:22px;color:var(--teal)}
.brand i{display:block;width:14px;height:14px;background:var(--teal)}
.nav{left:423px;top:38px;display:flex;gap:16px;font-size:12.5px;letter-spacing:.8px;color:#3d4347}
/* hero */
.hero{left:0;top:111px;width:1200px;height:438px;background:linear-gradient(160deg,#c9ccc6 0%,#8f8a7f 40%,#6d6a62 70%,#a7a9a2 100%)}
.hero-title{left:0;top:302px;width:1200px;text-align:center;font-family:"Josefin Sans",sans-serif;font-weight:400;font-size:31px;letter-spacing:4px;color:var(--white)}
.tile{top:466px;width:175px;height:185px;background:linear-gradient(180deg,var(--teal-light),var(--teal));border-bottom:4px solid var(--orange);color:var(--white);text-align:center}
.tile .ic{margin:14px auto 0;width:54px;height:54px;border-radius:50%;background:var(--white);display:flex;align-items:center;justify-content:center}
.tile .ic svg{width:30px;height:30px}
.tile h4{margin-top:16px;font-size:12px;font-weight:600;text-decoration:underline;letter-spacing:.3px}
.tile p{margin:6px 20px 0;font-size:11.5px;line-height:13px}
/* who */
.who-band{left:0;top:765px;width:1200px;height:278px;background:var(--teal)}
.who-photo{left:602px;top:739px;width:539px;height:335px;background:linear-gradient(180deg,#a9cde0 0%,#cfe0e6 35%,#d9c9a8 60%,#c7b48f 100%)}
.who-title{left:221px;top:838px;font-size:31px;color:var(--white);font-weight:400}
.who-text{left:231px;top:884px;width:285px;font-size:11.5px;line-height:16px;color:#e6f2f1;letter-spacing:.3px}
.outline-btn{position:absolute;border:2px solid var(--orange);color:var(--orange);font-weight:800;font-size:12px;letter-spacing:1px;display:flex;align-items:center;justify-content:center}
/* offer */
.offer-title{left:0;top:1166px;width:1200px;text-align:center;font-size:31px}
.card{width:362px;height:186px;display:flex}
.card .body{width:189px;background:var(--teal);color:var(--white);padding:22px 20px 0 23px;position:relative}
.card h3{font-weight:700;font-size:15px;letter-spacing:1.5px;line-height:17px}
.card p{margin-top:9px;font-size:11.5px;line-height:16px;color:#e3f0ef}
.card .go{position:absolute;left:23px;bottom:12px;width:20px;height:20px}
.card .pic{flex:1}
.rule{left:231px;top:1677px;width:737px;height:1px;background:var(--line)}
/* banner */
.banner{left:0;top:1776px;width:1200px;height:386px;background:linear-gradient(180deg,rgba(19,122,116,.85),rgba(19,122,116,.92)),linear-gradient(90deg,#5b6f6a,#8ea09b 50%,#4f605c)}
.banner-title{left:0;top:1902px;width:1200px;text-align:center;font-family:"Josefin Sans",sans-serif;font-weight:400;font-size:31px;line-height:37px;letter-spacing:4px;color:var(--white)}
/* news */
.news-title{left:228px;top:2238px;font-size:31px;color:var(--teal-dark)}
.news{left:231px;width:273px;height:202px;background:var(--teal)}
.news .pic{height:119px;position:relative}
.news .tag{position:absolute;left:8px;bottom:3px;font-size:8px;color:var(--white)}
.news h5{margin:6px 9px 0;font-size:11px;font-weight:800;color:var(--white)}
.news .date{margin:4px 9px 0;font-size:8px;color:#bfe0dc}
.news p{margin:4px 9px 0;font-size:10.5px;line-height:13px;color:var(--white)}
.offices{left:524px;top:2306px;width:471px;height:636px;border:1px solid var(--line);background:var(--white)}
.offices-title{left:524px;top:2350px;width:471px;text-align:center;font-family:"Josefin Sans",sans-serif;font-weight:300;font-size:30px;letter-spacing:4px;color:var(--teal)}
.map{left:585px;top:2440px;width:150px;height:420px;background:linear-gradient(180deg,var(--map-top),var(--map-bottom))}
.office{left:780px;font-size:11px;line-height:18px;color:#3d4347}
.office h6{font-size:14.5px;font-weight:700;color:var(--ink);line-height:18px}
.office .row{display:flex;align-items:center;gap:6px}
.office .row svg{width:12px;height:12px}
.office .indent{padding-left:18px}
/* contact */
.contact{left:0;top:3041px;width:1200px;height:406px;background:var(--mist)}
.contact-title{left:231px;top:3078px;font-size:31px;color:var(--teal-dark)}
.contact-text{left:231px;top:3126px;width:250px;font-size:11px;line-height:15px;color:#4a5256}
.consent{left:231px;top:3197px;width:255px;display:flex;gap:8px;font-size:11px;line-height:15px;color:#4a5256}
.consent span{flex:none;width:11px;height:11px;border:1px solid #b8c2c5;background:var(--white);margin-top:2px}
.label{left:543px;font-size:11px;color:#3d4347}
.field{left:606px;width:362px;height:30px;background:var(--white);border:1px solid var(--line);font-size:11px;color:#b9c0c3;padding:8px 14px}
.captcha{left:606px;top:3390px;font-size:10.5px;line-height:15px;color:var(--muted)}
.captcha u{color:var(--teal)}
/* footer */
.footer{left:0;top:3447px;width:1200px;height:273px;background:var(--teal-dark)}
.f-brand{left:231px;top:3508px;display:flex;align-items:center;gap:8px;font-weight:800;font-size:24px;color:var(--white)}
.f-brand i{display:block;width:14px;height:14px;background:var(--white)}
.f-text{left:231px;top:3580px;width:160px;font-size:11px;line-height:16px;color:#dfe8e7}
.f-col{top:3487px;font-size:11px;color:var(--white)}
.f-col h6{font-size:11.5px;font-weight:700;letter-spacing:1.5px;color:#2aa39a;margin-bottom:12px}
.f-col li{list-style:none;height:22px;font-weight:700;letter-spacing:1px;display:flex;align-items:center;gap:8px}
.f-col li.plain{font-weight:400;letter-spacing:0}
.f-col .sq{width:16px;height:16px;border:2px solid var(--white);border-radius:3px}
.f-col .ci{width:11px;height:11px}
.f-rule{left:231px;top:3682px;width:737px;height:1px;background:#2c5552}
.copy{left:0;top:3698px;width:1200px;text-align:center;font-size:10px;color:#8aa3a0}
.totop{left:905px;top:3697px;font-size:11px;font-weight:700;color:var(--white);display:flex;align-items:center;gap:6px}
</style>
</head>
<body>

<!-- top bar -->
<div class="abs topbar">
  <span class="abs social" style="left:231px"></span>
  <span class="abs social" style="left:260px;border-radius:50%"></span>
  <span class="abs social" style="left:289px"></span>
  <div class="abs join">Join ORVET &nbsp;♡</div>
  <div class="btn donate">DONATE NOW <svg viewBox="0 0 16 16" fill="none" stroke="#fff" stroke-width="1.6"><path d="M2 13c2-5 5-7 10-7M9 3l4 3-4 3"/></svg></div>
</div>

<!-- header -->
<header class="abs header">
  <div class="abs brand"><i></i>ORVET</div>
  <nav class="abs nav"><span>About Us</span><span>Programs</span><span>Rehabilitation &amp; Sports</span><span>Rights Realization</span><span>News</span><span>Contact Us</span></nav>
</header>

<!-- hero -->
<section class="abs hero" role="img" aria-label="Photo of friends greeting each other outdoors, one using a wheelchair"></section>
<h1 class="abs hero-title">A Good Life For Everyone, Like Everyone</h1>
<div class="btn" style="left:491px;top:348px;width:218px;height:29px">Donate to Help Us Help Them <svg viewBox="0 0 16 16" fill="none" stroke="#fff" stroke-width="1.6"><path d="M2 13c2-5 5-7 10-7M9 3l4 3-4 3"/></svg></div>

<div class="abs tile" style="left:231px">
  <div class="ic"><svg viewBox="0 0 30 30" fill="none" stroke="#137a74" stroke-width="1.6"><circle cx="11" cy="8" r="3"/><circle cx="20" cy="8" r="3"/><path d="M6 24v-8h10v8M15 24v-8h10v8"/></svg></div>
  <h4>I WANT TO KNOW</h4>
  <p>What are all the rights available to people with physical disabilities and their families</p>
</div>
<div class="abs tile" style="left:419px">
  <div class="ic"><svg viewBox="0 0 30 30" fill="none" stroke="#137a74" stroke-width="1.6"><rect x="5" y="7" width="20" height="13" rx="1"/><path d="M3 23h24M11 17l4-5 4 5"/></svg></div>
  <h4>I WANT TO KNOW</h4>
  <p>Where I can join online classes offered by ORVET</p>
</div>
<div class="abs tile" style="left:606px">
  <div class="ic"><svg viewBox="0 0 30 30" fill="none" stroke="#137a74" stroke-width="1.6"><path d="M6 18c3 4 8 6 13 3l5-6M8 12l5-5 4 4 4-3"/><circle cx="15" cy="14" r="2"/></svg></div>
  <h4>I WANT TO KNOW</h4>
  <p>What services there are for children with disabilities</p>
</div>
<div class="abs tile" style="left:794px">
  <div class="ic"><svg viewBox="0 0 30 30" fill="none" stroke="#137a74" stroke-width="1.6"><circle cx="10" cy="7" r="2.5"/><circle cx="20" cy="7" r="2.5"/><path d="M7 25V12h6v13M17 25V12h6v13M13 15h4"/></svg></div>
  <h4>I WANT TO KNOW</h4>
  <p>If there is a rehabilitation center in my area</p>
</div>

<!-- who we are -->
<section class="abs who-band"></section>
<div class="abs who-photo" role="img" aria-label="Photo of a man in a beach wheelchair at the seaside with volunteers"></div>
<h2 class="abs heading who-title">Who We Are</h2>
<p class="abs who-text">Find out what we're up to, our programs and our activities. Lorem ipsum dolor sit amet is a dummy text for placeholder purposes.</p>
<div class="outline-btn" style="left:231px;top:953px;width:113px;height:32px">ABOUT US</div>

<!-- what we offer -->
<h2 class="abs heading offer-title">What We Offer</h2>
<div class="abs card" style="left:231px;top:1248px">
  <div class="body"><h3>EDUCATION</h3><p>ORVET works to impart education and knowledge to people with disabilities and operates the dedicated campus ...</p>
    <svg class="go" viewBox="0 0 20 20" fill="none" stroke="#fff" stroke-width="1.4"><circle cx="10" cy="10" r="8.5"/><path d="M8.5 6.5 12 10l-3.5 3.5"/></svg></div>
  <div class="pic" role="img" aria-label="Photo of students studying together around a table" style="background:linear-gradient(135deg,#e9e4dc,#b9a592 60%,#7d8c86)"></div>
</div>
<div class="abs card" style="left:606px;top:1248px">
  <div class="body"><h3>SPORTS &amp; REHAB</h3><p>ORVET encourages people with disabilities to play sports and find new strengths in themselves...</p>
    <svg class="go" viewBox="0 0 20 20" fill="none" stroke="#fff" stroke-width="1.4"><circle cx="10" cy="10" r="8.5"/><path d="M8.5 6.5 12 10l-3.5 3.5"/></svg></div>
  <div class="pic" role="img" aria-label="Photo of a man exercising on rehabilitation gym equipment" style="background:linear-gradient(135deg,#dfe6ea,#8a9aa6 55%,#3f5c86)"></div>
</div>
<div class="abs card" style="left:231px;top:1449px">
  <div class="body"><h3>RIGHTS &amp;<br>REALIZATION</h3><p>ORVET promotes policies concerning people with physical-motor disabilities, promotes their rights, ....</p>
    <svg class="go" viewBox="0 0 20 20" fill="none" stroke="#fff" stroke-width="1.4"><circle cx="10" cy="10" r="8.5"/><path d="M8.5 6.5 12 10l-3.5 3.5"/></svg></div>
  <div class="pic" role="img" aria-label="Photo of an empty wheelchair on a sandy beach" style="background:linear-gradient(180deg,#bfe1ef,#d8e8ea 45%,#e7d9bf)"></div>
</div>
<div class="abs card" style="left:606px;top:1449px">
  <div class="body"><h3>COMMUNITY &amp;<br>INFRASTRUCTURE</h3><p>ORVET owns the associations houses all over the country, rehabilitation day centers,...</p>
    <svg class="go" viewBox="0 0 20 20" fill="none" stroke="#fff" stroke-width="1.4"><circle cx="10" cy="10" r="8.5"/><path d="M8.5 6.5 12 10l-3.5 3.5"/></svg></div>
  <div class="pic" role="img" aria-label="Photo of friends sharing drinks at a community gathering" style="background:linear-gradient(135deg,#5a4a3c,#8b7a66 50%,#4a3e35)"></div>
</div>
<div class="abs rule"></div>

<!-- banner -->
<section class="abs banner" role="img" aria-label="Photo of athletes on crutches playing on an outdoor sports court, with a teal overlay"></section>
<h2 class="abs banner-title">Even People With Disabilities Can Be<br>With Everyone, Like Everyone</h2>
<div class="btn" style="left:485px;top:1998px;width:220px;height:29px">Don't Leave Them Behind <svg viewBox="0 0 16 16" fill="none" stroke="#fff" stroke-width="1.6"><path d="M2 13c2-5 5-7 10-7M9 3l4 3-4 3"/></svg></div>

<!-- news -->
<h2 class="abs heading news-title">Latest News</h2>
<article class="abs news" style="top:2305px">
  <div class="pic" role="img" aria-label="Photo of two people embracing in a support session" style="background:linear-gradient(135deg,#e8e2db,#b79a85 55%,#6e5b4f)"><span class="tag">Mental Health</span></div>
  <h5>Group Sharing Sessions In Riverside</h5><div class="date">26 Aug 2023</div>
  <p>Ipsum dolor sit amet, consectetur adipiscing elit, sed do eiusmod tempor incididunt ut</p>
</article>
<article class="abs news" style="top:2523px">
  <div class="pic" role="img" aria-label="Photo of runners at a marathon event" style="background:linear-gradient(135deg,#d8e6ee,#d9a85c 45%,#b94a34 70%,#7f8a90)"><span class="tag">Events</span></div>
  <h5>Annual Marathon Event</h5><div class="date">26 Aug 2023</div>
  <p>Ipsum dolor sit amet, consectetur adipiscing elit, sed do eiusmod tempor incididunt ut</p>
</article>
<article class="abs news" style="top:2741px">
  <div class="pic" role="img" aria-label="Photo of two people talking in a park, one in a wheelchair" style="background:linear-gradient(135deg,#2f4a2c,#6f8a5a 50%,#c9d2c1)"><span class="tag">Events</span></div>
  <h5>World Disability Awareness Day</h5><div class="date">26 Aug 2023</div>
  <p>Ipsum dolor sit amet, consectetur adipiscing elit, sed do eiusmod tempor incididunt ut</p>
</article>
<div class="outline-btn" style="left:231px;top:2957px;width:157px;height:31px;font-weight:700;letter-spacing:0;font-size:12px">View All News &nbsp;›</div>

<section class="abs offices"></section>
<h2 class="abs offices-title">Our Office Branches</h2>
<div class="abs map" role="img" aria-label="Map of the country showing the office branch locations"></div>

<div class="abs office" style="top:2433px">
  <h6>Head Office</h6>
  <div class="row"><svg viewBox="0 0 12 12"><circle cx="6" cy="6" r="6" fill="#137a74"/><path d="M4 3.5l1 1.5-.6.7c.4.8 1 1.4 1.8 1.8l.7-.6 1.5 1-.5 1C5.6 9 3 6.4 3 4z" fill="#fff"/></svg>03-5550142</div>
  <div class="row"><svg viewBox="0 0 12 12"><circle cx="6" cy="6" r="6" fill="#137a74"/><path d="M6 2.5a2.2 2.2 0 0 1 2.2 2.2C8.2 6.3 6 9.5 6 9.5S3.8 6.3 3.8 4.7A2.2 2.2 0 0 1 6 2.5z" fill="#fff"/></svg>12 Cedar Lane</div>
  <div class="indent">PO Box 4810</div><div class="indent">Harbor Town&nbsp; 4700215</div>
</div>
<div class="abs office" style="top:2585px">
  <h6>Office No. 2</h6>
  <div class="row"><svg viewBox="0 0 12 12"><circle cx="6" cy="6" r="6" fill="#137a74"/><path d="M4 3.5l1 1.5-.6.7c.4.8 1 1.4 1.8 1.8l.7-.6 1.5 1-.5 1C5.6 9 3 6.4 3 4z" fill="#fff"/></svg>03-5550142</div>
  <div class="row"><svg viewBox="0 0 12 12"><circle cx="6" cy="6" r="6" fill="#137a74"/><path d="M6 2.5a2.2 2.2 0 0 1 2.2 2.2C8.2 6.3 6 9.5 6 9.5S3.8 6.3 3.8 4.7A2.2 2.2 0 0 1 6 2.5z" fill="#fff"/></svg>12 Cedar Lane</div>
  <div class="indent">PO Box 4810</div><div class="indent">Harbor Town&nbsp; 4700215</div>
</div>
<div class="abs office" style="top:2737px">
  <h6>Office No. 3</h6>
  <div class="row"><svg viewBox="0 0 12 12"><circle cx="6" cy="6" r="6" fill="#137a74"/><path d="M4 3.5l1 1.5-.6.7c.4.8 1 1.4 1.8 1.8l.7-.6 1.5 1-.5 1C5.6 9 3 6.4 3 4z" fill="#fff"/></svg>03-5550142</div>
  <div class="row"><svg viewBox="0 0 12 12"><circle cx="6" cy="6" r="6" fill="#137a74"/><path d="M6 2.5a2.2 2.2 0 0 1 2.2 2.2C8.2 6.3 6 9.5 6 9.5S3.8 6.3 3.8 4.7A2.2 2.2 0 0 1 6 2.5z" fill="#fff"/></svg>12 Cedar Lane</div>
  <div class="indent">PO Box 4810</div><div class="indent">Harbor Town&nbsp; 4700215</div>
</div>

<!-- contact -->
<section class="abs contact"></section>
<h2 class="abs heading contact-title">Contact Us</h2>
<p class="abs contact-text">Ipsum dolor sit amet, consectetur adipiscing elit, sed do eiusmod tempor incididunt ut labore et dolore magna aliqua. Quis ipsum</p>
<div class="abs consent"><span></span><p>I know that the details I provided are stored in Orvet's databases, subject to the rules of privacy protection and information security and in accordance with the privacy policy detailed on the website</p></div>

<div class="abs label" style="top:3088px">Name*</div><div class="abs field" style="top:3079px">Name</div>
<div class="abs label" style="top:3132px">Email*</div><div class="abs field" style="top:3123px">Email Address</div>
<div class="abs label" style="top:3179px">Phone*</div><div class="abs field" style="top:3170px">Phone Number</div>
<div class="abs label" style="top:3222px">Message</div><div class="abs field" style="top:3214px;height:119px">Type your message here</div>
<div class="btn" style="left:606px;top:3346px;width:155px;height:30px">Submit ›</div>
<p class="abs captcha">This site is protected by BotGuard and the SearchCo<br><u>Privacy Policy</u> and <u>Terms of Service</u> apply.</p>

<!-- footer -->
<footer class="abs footer"></footer>
<div class="abs f-brand"><i></i>ORVET</div>
<p class="abs f-text">The Orvet Association strives to enable people with physical disabilities to live meaningful and high-quality lives.</p>

<div class="abs f-col" style="left:448px"><h6>QUICK LINKS</h6>
  <ul><li>About Us</li><li>Programs</li><li>Rehabilitation &amp; Sports</li><li>Rights Realization</li><li>News</li><li>Contact Us</li></ul></div>
<div class="abs f-col" style="left:644px"><h6>SOCIAL MEDIA</h6>
  <ul style="line-height:1"><li style="height:34px"><span class="sq"></span>Linkup</li><li style="height:34px"><span class="sq" style="border-radius:50%"></span>Chirper</li><li style="height:34px"><span class="sq"></span>Picturely</li></ul></div>
<div class="abs f-col" style="left:819px"><h6>CONTACT INFO</h6>
  <ul>
    <li class="plain"><svg class="ci" viewBox="0 0 12 12"><circle cx="6" cy="6" r="6" fill="#fff"/><path d="M3 4h6v4H3zM3 4l3 2.2L9 4" fill="none" stroke="#0c3330" stroke-width=".9"/></svg>hello@orvet-example.org</li>
    <li class="plain"><svg class="ci" viewBox="0 0 12 12"><circle cx="6" cy="6" r="6" fill="#fff"/><path d="M4 3.5l1 1.5-.6.7c.4.8 1 1.4 1.8 1.8l.7-.6 1.5 1-.5 1C5.6 9 3 6.4 3 4z" fill="#0c3330"/></svg>03-5550187</li>
    <li class="plain"><svg class="ci" viewBox="0 0 12 12"><circle cx="6" cy="6" r="6" fill="#fff"/><path d="M4 3.5l1 1.5-.6.7c.4.8 1 1.4 1.8 1.8l.7-.6 1.5 1-.5 1C5.6 9 3 6.4 3 4z" fill="#0c3330"/></svg>03-5550142</li>
    <li class="plain"><svg class="ci" viewBox="0 0 12 12"><circle cx="6" cy="6" r="6" fill="#fff"/><path d="M6 2.5a2.2 2.2 0 0 1 2.2 2.2C8.2 6.3 6 9.5 6 9.5S3.8 6.3 3.8 4.7A2.2 2.2 0 0 1 6 2.5z" fill="#0c3330"/></svg>12 Cedar Lane</li>
    <li class="plain" style="padding-left:19px;height:18px">PO Box 4810</li>
    <li class="plain" style="padding-left:19px;height:18px">Harbor Town&nbsp; 4700215</li>
  </ul></div>

<div class="abs f-rule"></div>
<div class="abs copy">© 2023 All Rights Reserved</div>
<div class="abs totop">To Top <svg width="14" height="14" viewBox="0 0 14 14" fill="none" stroke="#fff" stroke-width="1.2"><circle cx="7" cy="7" r="6"/><path d="M4.5 8 7 5.5 9.5 8"/></svg></div>

</body>
</html>
```